Wordpress Website Design - Scroll Style

Digital marketing agency needs a website redesign and installation of design. Website is built on Wordpress so the designer should keep Wordpress in mind. We have included images, Homepage copy, Customer Experience page copy, What We Do page copy, documents and a read me file to help guide the design.

Target Market(s)

Franchise owners and Local business owners with 10+ locations.

Industry/Entity Type

Marketing

Coding

Coded - Design and coding required

Number of Pages Required

3 page

Font styles to use
Sans Serif

Requirements
Must have
• Must incorporate the website copy and other images and files uploaded. Must resize for mobile friendly use with easy to read font and font size. Scroll style website. Editable text rather than text embedded in an image.
Nice to have
• na
Should not have
• na

```html
<!DOCTYPE html>
<html lang="en">
<head>
<meta charset="utf-8">
<title>Summit Reach Marketing</title>
<link href="https://fonts.googleapis.com/css2?family=Open+Sans:wght@400;600;700&family=Raleway:wght@400;500;600&display=swap" rel="stylesheet">
<style>
:root{
  --blue:#1b8fd6;
  --blue-dark:#135f9e;
  --navy:#1d4e86;
  --ink:#2b2b2b;
  --muted:#707070;
  --line:#d8dde3;
  --panel:#f4f6f8;
  --black:#0b0b0b;
  --white:#ffffff;
  --grey-bg:#efefef;
  --star:#f5b800;
  --orange:#e67e22;
}
*{box-sizing:border-box;margin:0;padding:0}
html,body{width:1200px;height:3586px;overflow:hidden}
body{position:relative;font-family:"Open Sans",Arial,sans-serif;color:var(--ink);background:var(--white)}
.abs{position:absolute}
.raleway{font-family:"Raleway","Open Sans",sans-serif}

/* header */
.site-header{position:absolute;left:0;top:0;width:1200px;height:100px;background:var(--white)}
.brand{position:absolute;left:70px;top:30px;display:flex;align-items:center;gap:10px;color:var(--navy);font-family:"Raleway",sans-serif;font-weight:600;font-size:19px;letter-spacing:.5px}
.brand-dot{width:14px;height:14px;border-radius:50%;background:var(--blue)}
.account-links{position:absolute;right:100px;top:20px;display:flex;gap:36px;font-size:13px;font-weight:600;color:#222}
.account-links span{display:flex;align-items:center;gap:6px}
.main-nav{position:absolute;left:287px;top:67px;width:913px;height:33px;background:var(--blue);display:flex}
.main-nav a{flex:1;color:var(--white);text-decoration:none;font-size:12px;font-weight:600;text-align:center;line-height:33px}
.main-nav a.active{background:var(--blue-dark)}

/* hero */
.hero{position:absolute;left:0;top:100px;width:1200px;height:512px;background:linear-gradient(180deg,#4a4a4a 0%,#2c2c2c 55%,#1c1c1c 100%)}
.hero-title{position:absolute;left:0;width:1200px;top:110px;text-align:center;color:var(--white);font-weight:700;font-size:31px;line-height:64px}
.hero-sub{position:absolute;left:0;width:1200px;top:250px;text-align:center;color:var(--white);font-size:27px}
.hero-arrow{position:absolute;top:190px;width:40px;height:40px;border-radius:50%;border:2px solid rgba(255,255,255,.7);background:rgba(0,0,0,.35)}
.hero-tabs{position:absolute;left:131px;top:430px;width:935px;height:48px;display:flex}
.hero-tabs div{flex:1;display:flex;align-items:center;justify-content:center;font-size:16px;font-weight:600;color:var(--white)}
.tab-blue{background:linear-gradient(180deg,#2c9ae0,#1a73b8)}
.tab-black{background:var(--black)}

/* results */
.results-title{position:absolute;left:131px;top:664px;width:440px;font-family:"Raleway",sans-serif;font-size:22px;line-height:32px;color:#333}
.results-copy{position:absolute;left:131px;top:745px;width:430px;font-size:12.5px;line-height:22px;color:var(--muted);text-align:justify}
.btn-read{position:absolute;left:131px;top:908px;width:118px;height:40px;background:var(--navy);color:var(--white);font-size:12px;font-weight:700;display:flex;align-items:center;justify-content:center;gap:6px}
.card{position:absolute;background:var(--white);border:1px solid var(--line);box-shadow:0 3px 10px rgba(0,0,0,.18)}
.card-head{height:26px;background:#2e76a8;color:var(--white);font-size:13px;line-height:26px;padding-left:8px}
.mini{position:absolute;border:1px solid var(--line);background:var(--white)}
.mini-h{background:#e9eef3;font-size:11px;color:#2e76a8;padding:3px 6px}
.mini-n{font-size:36px;color:#2e76a8;font-weight:600;text-align:center}

/* what we do */
.wwd{position:absolute;left:0;top:992px;width:1200px;height:626px;background:var(--grey-bg)}
.section-title{position:absolute;left:0;width:1200px;text-align:center;font-family:"Raleway",sans-serif;font-size:27px;color:#333}
.wwd-intro{position:absolute;left:320px;top:90px;width:560px;text-align:center;font-size:12px;line-height:24px;color:var(--muted)}
.service{position:absolute;width:300px;text-align:center}
.service-icon{width:90px;height:90px;border-radius:50%;background:#3b3b3b;margin:0 auto 14px;display:flex;align-items:center;justify-content:center}
.service-icon.accent{background:var(--blue)}
.service h3{font-size:16px;font-weight:600;color:#333;margin-bottom:8px}
.service h3.accent{color:var(--blue)}
.service p{font-size:12px;line-height:22px;color:var(--muted)}

/* stats */
.stats{position:absolute;left:0;top:1618px;width:1200px;height:378px;background:linear-gradient(180deg,#6f7c88 0%,#9aa5ae 50%,#7b858d 100%)}
.stat{position:absolute;width:200px;height:200px;border-radius:50%;text-align:center;color:var(--white)}
.stat-inner{position:absolute;left:18px;top:18px;width:164px;height:164px;border-radius:50%;background:var(--navy);display:flex;flex-direction:column;align-items:center;justify-content:center}
.stat-num{font-size:32px;font-weight:400}
.stat-label{font-size:10px;letter-spacing:.3px;margin-top:4px}

/* realtime */
.realtime{position:absolute;left:0;top:1996px;width:1200px;height:872px;background:#f1f1f1}
.feature-label{position:absolute;font-family:"Raleway",sans-serif;font-size:23px;color:#2f8fd0}
.feature-copy{position:absolute;font-size:12.5px;line-height:20px;color:var(--muted)}
.t-row{display:flex;font-size:9px;color:#555;border-bottom:1px solid #eee;height:13px;line-height:13px}
.t-row span{flex:1;padding-left:4px}

/* cta */
.cta{position:absolute;left:0;top:2868px;width:1200px;height:112px;background:var(--black)}
.cta-text{position:absolute;left:155px;top:40px;color:var(--white);font-size:22px;letter-spacing:.5px}
.cta-btn{position:absolute;left:841px;top:34px;width:201px;height:46px;background:var(--blue);color:var(--white);font-size:19px;font-weight:600;display:flex;align-items:center;justify-content:center}

/* clients */
.clients-title{top:3030px}
.client{position:absolute;top:3088px;width:180px;height:92px;background:var(--white);box-shadow:0 1px 4px rgba(0,0,0,.2);display:flex;align-items:center;justify-content:center;font-size:24px;font-weight:700;color:#222}
.client-arrow{position:absolute;top:3100px}

/* testimonials */
.testimonials{position:absolute;left:0;top:3238px;width:1200px;height:288px;background:linear-gradient(180deg,#1d3e63 0%,#27557d 60%,#1f4a3f 100%)}
.bubble{position:absolute;top:108px;width:290px;height:88px;background:var(--black);color:var(--white);font-size:11.5px;line-height:19px;padding:10px 14px}
.bubble::after{content:"";position:absolute;left:22px;bottom:-10px;border:10px solid transparent;border-bottom:0;border-top-color:var(--black)}
.author{position:absolute;top:204px;display:flex;align-items:center;gap:10px;color:var(--white);font-size:11px}
.avatar{width:32px;height:32px;background:#8c8f93;border:2px solid var(--white)}
.footer{position:absolute;left:0;top:3526px;width:1200px;height:60px;background:#1e1e1e;color:#ccc;font-size:11px;text-align:center;line-height:60px}
</style>
</head>
<body>

<header class="site-header">
  <div class="brand"><span class="brand-dot"></span>SUMMIT REACH MARKETING</div>
  <div class="account-links">
    <span><svg width="10" height="11" viewBox="0 0 10 11"><circle cx="5" cy="3" r="2.6" fill="#222"/><path d="M0 11c0-3 2-5 5-5s5 2 5 5z" fill="#222"/></svg>LOG IN</span>
    <span><svg width="11" height="11" viewBox="0 0 11 11"><circle cx="4.5" cy="3" r="2.6" fill="#222"/><path d="M0 11c0-3 2-5 4.5-5S9 8 9 11z" fill="#222"/><path d="M8 1h3M9.5-.5v3" stroke="#222"/></svg>SIGNUP</span>
  </div>
  <nav class="main-nav">
    <a class="active">FEATURES</a><a>PRICING</a><a>FORUM</a><a>RESOURCES</a><a>BLOG</a><a>PARTNERS</a>
  </nav>
</header>

<section class="hero" role="img" aria-label="Dimmed photo of a laptop showing marketing charts on a desk">
  <div class="hero-title">Overwhelmed by your online marketing<br>efforts and underwhelmed by results?</div>
  <div class="hero-sub">We track and manage every online marketing action</div>
  <div class="hero-arrow" style="left:96px"><svg width="36" height="36" viewBox="0 0 36 36"><path d="M21 11l-7 7 7 7" stroke="#fff" stroke-width="3" fill="none"/></svg></div>
  <div class="hero-arrow" style="left:1062px"><svg width="36" height="36" viewBox="0 0 36 36"><path d="M15 11l7 7-7 7" stroke="#fff" stroke-width="3" fill="none"/></svg></div>
  <div class="hero-tabs">
    <div class="tab-blue">Results Driven</div>
    <div class="tab-black">Minimal Time Commitment</div>
    <div class="tab-blue">Affordable</div>
    <div class="tab-black">Clear Reporting</div>
  </div>
</section>

<h2 class="results-title">Results-Driven Digital Marketing for Your Local Business</h2>
<p class="results-copy">Digital marketing is critical for your local business. According to Searchwell, 97% of consumers use the Internet to search for local businesses. Yet, making your way through the dizzying maze of Rateline, Searchwell rankings, AdPlace, promotions, and advertising can be time consuming and frustrating - especially when you have no insight into what's working and, equally important, what's not working.</p>
<div class="btn-read">READ MORE <svg width="12" height="12" viewBox="0 0 12 12"><circle cx="6" cy="6" r="6" fill="#fff"/><path d="M5 3l3 3-3 3" stroke="#1d4e86" stroke-width="1.6" fill="none"/></svg></div>

<div class="card" style="left:590px;top:652px;width:545px;height:300px">
  <div class="card-head">Call Tracking</div>
  <div class="mini" style="left:8px;top:34px;width:168px;height:70px"><div class="mini-h">Total Calls</div><div class="mini-n">255</div></div>
  <div class="mini" style="left:8px;top:112px;width:168px;height:70px"><div class="mini-h">Answered Calls</div><div class="mini-n">207</div></div>
  <div class="mini" style="left:8px;top:190px;width:168px;height:70px"><div class="mini-h">Not Answered</div><div class="mini-n">48</div></div>
  <div class="mini" style="left:186px;top:34px;width:180px;height:256px">
    <div class="mini-h">Call Log</div>
    <div class="t-row"><span>Number</span><span>Src</span><span>Dur</span></div>
    <div class="t-row"><span>555-0101</span><span>Web</span><span>2:14</span></div>
    <div class="t-row"><span>555-0102</span><span>Ads</span><span>1:05</span></div>
    <div class="t-row"><span>555-0103</span><span>Web</span><span>3:40</span></div>
    <div class="t-row"><span>555-0104</span><span>Map</span><span>0:52</span></div>
    <div class="t-row"><span>555-0105</span><span>Ads</span><span>4:11</span></div>
    <div class="t-row"><span>555-0106</span><span>Web</span><span>1:33</span></div>
    <div class="t-row"><span>555-0107</span><span>Map</span><span>2:08</span></div>
    <div class="t-row"><span>555-0108</span><span>Ads</span><span>0:47</span></div>
    <div class="t-row"><span>555-0109</span><span>Web</span><span>3:02</span></div>
    <div class="t-row"><span>555-0110</span><span>Map</span><span>1:19</span></div>
    <div style="font-size:9px;color:#2e76a8;text-align:center;margin-top:8px">See All</div>
  </div>
  <div class="mini" style="left:374px;top:34px;width:162px;height:100px">
    <div class="mini-h">Calls vs. Days</div>
    <svg width="160" height="76" viewBox="0 0 160 76"><g fill="#2e5fb8"><rect x="22" y="48" width="8" height="20"/><rect x="36" y="38" width="8" height="30"/><rect x="50" y="44" width="8" height="24"/><rect x="64" y="30" width="8" height="38"/><rect x="78" y="52" width="8" height="16"/><rect x="92" y="22" width="8" height="46"/><rect x="106" y="40" width="8" height="28"/><rect x="120" y="10" width="8" height="58"/></g><line x1="14" y1="68" x2="140" y2="68" stroke="#999"/></svg>
  </div>
  <div class="mini" style="left:374px;top:144px;width:162px;height:100px">
    <div class="mini-h">Top 5 Numbers</div>
    <div class="t-row"><span>Number</span><span># of Calls</span></div>
    <div class="t-row"><span>Main</span><span>65</span></div>
    <div class="t-row"><span>West</span><span>52</span></div>
    <div class="t-row"><span>North</span><span>36</span></div>
    <div class="t-row"><span>Harbor</span><span>22</span></div>
  </div>
</div>

<section class="wwd">
  <h2 class="section-title" style="top:42px">What We DO</h2>
  <p class="wwd-intro">Summit Reach is a Digital Marketing platform and service provider focused on managing and controlling the online presence of franchisors and franchisees of local businesses from one easy-to-use interface so you can:</p>

  <div class="service" style="left:137px;top:165px">
    <div class="service-icon accent"><svg width="44" height="44" viewBox="0 0 44 44"><path d="M34 10H20a12 12 0 0 0 0 24h14v-8H20a4 4 0 0 1 0-8h14z" fill="#fff"/></svg></div>
    <h3 class="accent">ATTRACT CUSTOMERS</h3>
    <p>Attract new customers through targeted and optimized online marketing programs and reputation management</p>
  </div>
  <div class="service" style="left:448px;top:165px">
    <div class="service-icon"><svg width="44" height="44" viewBox="0 0 44 44"><g fill="#fff"><rect x="8" y="28" width="6" height="10"/><rect x="17" y="22" width="6" height="16"/><rect x="26" y="16" width="6" height="22"/><rect x="35" y="10" width="4" height="28"/></g><path d="M6 24L30 6" stroke="#fff" stroke-width="2"/></svg></div>
    <h3>GROW REVENUE</h3>
    <p>Grow the lifetime value of your customers by leveraging automated nurture and retention campaigns through email.</p>
  </div>
  <div class="service" style="left:787px;top:165px">
    <div class="service-icon"><svg width="44" height="44" viewBox="0 0 44 44"><rect x="12" y="6" width="20" height="32" rx="3" fill="#fff"/><circle cx="22" cy="20" r="6" fill="#3b3b3b"/><text x="22" y="24" font-size="10" text-anchor="middle" fill="#fff" font-family="Open Sans, sans-serif">$</text></svg></div>
    <h3>REDUCE COSTS</h3>
    <p>Cut costs by automating many daily management tasks and identifying real time service issues that need attention</p>
  </div>
  <div class="service" style="left:271px;top:372px">
    <div class="service-icon"><svg width="44" height="44" viewBox="0 0 44 44"><circle cx="22" cy="15" r="8" fill="#fff"/><path d="M8 40c0-9 6-14 14-14s14 5 14 14z" fill="#fff"/></svg></div>
    <h3>DELIGHT CLIENTS</h3>
    <p>Make it a two-way conversation by providing your customers the forum to provide feedback on a consistent basis</p>
  </div>
  <div class="service" style="left:617px;top:372px">
    <div class="service-icon"><svg width="44" height="44" viewBox="0 0 44 44"><rect x="6" y="8" width="32" height="22" rx="2" fill="none" stroke="#fff" stroke-width="3"/><rect x="18" y="32" width="8" height="4" fill="#fff"/><circle cx="30" cy="30" r="7" fill="#fff"/><circle cx="30" cy="30" r="3" fill="#3b3b3b"/></svg></div>
    <h3>VISUALIZE &amp; MEASURE</h3>
    <p>Through our innovative platform you get inside your marketing programs with a real-time view of campaigns, leads and ROI</p>
  </div>
</section>

<section class="stats" role="img" aria-label="Blurred photo of a street scene behind the statistics">
  <div class="stat" style="left:100px;top:80px"><svg class="abs" width="200" height="200" viewBox="0 0 200 200"><circle cx="100" cy="100" r="95" fill="none" stroke="#1b8fd6" stroke-width="10" stroke-dasharray="450 597" transform="rotate(-90 100 100)"/></svg><div class="stat-inner"><div class="stat-num">248</div><div class="stat-label">SATISFIED CLIENTS</div></div></div>
  <div class="stat" style="left:337px;top:80px"><svg class="abs" width="200" height="200" viewBox="0 0 200 200"><circle cx="100" cy="100" r="95" fill="none" stroke="#1b8fd6" stroke-width="10" stroke-dasharray="500 597" transform="rotate(-90 100 100)"/></svg><div class="stat-inner"><div class="stat-num">89500</div><div class="stat-label">COUPON RECEIVED</div></div></div>
  <div class="stat" style="left:605px;top:80px"><svg class="abs" width="200" height="200" viewBox="0 0 200 200"><circle cx="100" cy="100" r="95" fill="none" stroke="#1b8fd6" stroke-width="10" stroke-dasharray="420 597" transform="rotate(-90 100 100)"/></svg><div class="stat-inner"><div class="stat-num">268688</div><div class="stat-label">CALLS GENRATED</div></div></div>
  <div class="stat" style="left:868px;top:80px"><svg class="abs" width="200" height="200" viewBox="0 0 200 200"><circle cx="100" cy="100" r="95" fill="none" stroke="#1b8fd6" stroke-width="10" stroke-dasharray="470 597" transform="rotate(-90 100 100)"/></svg><div class="stat-inner"><div class="stat-num">118385</div><div class="stat-label">SOCIAL POST</div></div></div>
</section>

<section class="realtime">
  <h2 class="section-title" style="top:28px;font-size:25px">See Your Marketing Dollars at Work in Real Time</h2>

  <div class="card" style="left:136px;top:98px;width:584px;height:370px">
    <div class="card-head">Review Mangement</div>
    <div class="mini" style="left:8px;top:36px;width:176px;height:76px"><div class="mini-h">Surveys Sent</div><div class="mini-n" style="color:#222">23</div></div>
    <div class="mini" style="left:8px;top:120px;width:176px;height:76px"><div class="mini-h">Responses</div><div class="mini-n" style="color:#222">16</div></div>
    <div class="mini" style="left:8px;top:204px;width:176px;height:76px"><div class="mini-h">Internal Reviews</div>
      <svg width="170" height="30" viewBox="0 0 170 30"><g fill="#f5b800"><polygon points="20,5 23,13 31,13 25,18 27,26 20,21 13,26 15,18 9,13 17,13"/><polygon points="40,5 43,13 51,13 45,18 47,26 40,21 33,26 35,18 29,13 37,13"/><polygon points="60,5 63,13 71,13 65,18 67,26 60,21 53,26 55,18 49,13 57,13"/><polygon points="80,5 83,13 91,13 85,18 87,26 80,21 73,26 75,18 69,13 77,13"/></g></svg>
      <div style="font-size:8px;color:#777;text-align:center">4.5 Stars Based on 2 Reviews</div></div>
    <div class="mini" style="left:196px;top:36px;width:180px;height:170px"><div class="mini-h">Survey Log</div>
      <div class="t-row"><span>Name</span><span>Rating</span><span>Date</span></div>
      <div class="t-row"><span>Alex Moore</span><span>4.5</span><span>7/14</span></div>
      <div class="t-row"><span>Lea Park</span><span>5</span><span>7/12</span></div>
      <div class="t-row"><span>Sam Ortiz</span><span>4</span><span>7/09</span></div>
      <div class="t-row"><span>Rina Cole</span><span>4.5</span><span>7/05</span></div>
    </div>
    <div class="mini" style="left:386px;top:36px;width:186px;height:90px"><div class="mini-h">Rateline Reviews</div>
      <svg width="184" height="30" viewBox="0 0 184 30"><g fill="#f5b800"><polygon points="50,5 53,13 61,13 55,18 57,26 50,21 43,26 45,18 39,13 47,13"/><polygon points="70,5 73,13 81,13 75,18 77,26 70,21 63,26 65,18 59,13 67,13"/><polygon points="90,5 93,13 101,13 95,18 97,26 90,21 83,26 85,18 79,13 87,13"/><polygon points="110,5 113,13 121,13 115,18 117,26 110,21 103,26 105,18 99,13 107,13"/></g></svg>
      <div style="font-size:8px;color:#555;text-align:center">4.4 Stars Based on 35 Reviews</div></div>
  </div>

  <div class="card" style="left:136px;top:482px;width:430px;height:330px">
    <div class="card-head" style="background:#111">Leads</div>
    <div class="mini" style="left:8px;top:34px;width:176px;height:80px"><div class="mini-h">Leads <span style="float:right;font-size:8px">(last 30 days)</span></div><div class="mini-n">48</div></div>
    <div class="mini" style="left:8px;top:122px;width:176px;height:80px"><div class="mini-h">Organic <span style="float:right;font-size:8px">(last 30 days)</span></div><div class="mini-n">36</div></div>
    <div class="mini" style="left:8px;top:210px;width:176px;height:80px"><div class="mini-h">Paid <span style="float:right;font-size:8px">(last 30 days)</span></div><div class="mini-n">12</div></div>
    <div class="mini" style="left:196px;top:34px;width:180px;height:256px;padding-top:96px">
      <div class="t-row"><span>Web</span><span>Social</span><span>7/14</span></div>
      <div class="t-row"><span>Call</span><span>Organic</span><span>7/13</span></div>
      <div class="t-row"><span>Web</span><span>Search</span><span>7/11</span></div>
      <div class="t-row"><span>Email</span><span>Social</span><span>7/10</span></div>
      <div class="t-row"><span>Web</span><span>Organic</span><span>7/08</span></div>
      <div class="t-row"><span>Call</span><span>Social</span><span>7/06</span></div>
      <div style="font-size:9px;color:#2e76a8;text-align:center;margin-top:16px">See All</div>
    </div>
    <svg class="abs" style="left:386px;top:180px" width="140" height="120" viewBox="0 0 140 120"><g fill="#2433a8"><rect x="10" y="70" width="16" height="40"/><rect x="40" y="40" width="16" height="70"/><rect x="70" y="54" width="16" height="56"/><rect x="100" y="6" width="16" height="104"/></g><line x1="0" y1="110" x2="130" y2="110" stroke="#999"/></svg>
  </div>

  <div class="card" style="left:327px;top:270px;width:562px;height:326px">
    <div class="card-head" style="background:#111">ROI</div>
    <div class="mini" style="left:8px;top:34px;width:180px;height:80px"><div class="mini-h">Total Revenue Generated</div><div class="mini-n" style="color:#222;font-size:32px">$25,800</div></div>
    <div class="mini" style="left:8px;top:124px;width:180px;height:76px"><div class="mini-h">Total Spend</div><div class="mini-n" style="color:#222;font-size:32px">$5,650</div></div>
    <div class="mini" style="left:8px;top:210px;width:180px;height:80px"><div class="mini-h">ROI</div><div class="mini-n" style="color:#1e9e4a">21%</div></div>
    <div class="mini" style="left:198px;top:34px;width:350px;height:130px"><div class="mini-h">Revenue vs. Spend</div>
      <svg width="348" height="104" viewBox="0 0 348 104"><g stroke="#e3e3e3"><line x1="40" y1="20" x2="260" y2="20"/><line x1="40" y1="45" x2="260" y2="45"/><line x1="40" y1="70" x2="260" y2="70"/></g><path d="M40 78L110 60L170 40L260 14V92H40z" fill="#b8d9a8"/><path d="M40 86L110 82L170 74L260 66V92H40z" fill="#3a74a8"/><line x1="40" y1="92" x2="260" y2="92" stroke="#999"/><rect x="272" y="20" width="10" height="6" fill="#b8d9a8"/><rect x="272" y="32" width="10" height="6" fill="#3a74a8"/></svg></div>
    <div class="mini" style="left:198px;top:174px;width:170px;height:120px"><div class="mini-h">Opportunity Costs</div>
      <div style="font-size:32px;font-weight:700;color:var(--orange);text-align:center;margin-top:6px">$6.95</div>
      <div style="font-size:10px;color:#777;text-align:center">avg. last month</div>
      <div style="font-size:10px;color:#333;text-align:center;margin-top:4px"><b>$14.60 avg</b> Since 5/1/2015</div></div>
    <div class="mini" style="left:378px;top:174px;width:170px;height:120px"><div class="mini-h">Revenue by Source</div>
      <svg width="168" height="94" viewBox="0 0 168 94"><g fill="#2433a8"><rect x="22" y="10" width="14" height="70"/><rect x="48" y="48" width="14" height="32"/><rect x="74" y="58" width="14" height="22"/><rect x="100" y="30" width="14" height="50"/><rect x="126" y="64" width="14" height="16"/></g><line x1="14" y1="80" x2="150" y2="80" stroke="#999"/></svg></div>
  </div>

  <svg class="abs" style="left:940px;top:112px" width="56" height="56" viewBox="0 0 56 56"><polygon points="28,4 34,20 52,20 38,31 43,49 28,38 13,49 18,31 4,20 22,20" fill="none" stroke="#2f8fd0" stroke-width="3"/></svg>
  <svg class="abs" style="left:740px;top:168px" width="160" height="50" viewBox="0 0 160 50"><path d="M0 48L150 2" stroke="#7fb6df" stroke-width="1.4"/></svg>
  <div class="feature-label" style="left:796px;top:178px">Manage Reviews</div>
  <div class="feature-copy" style="left:757px;top:208px;width:320px;text-align:center">Identify the total revenue generated<br>vs. your campaign spend</div>

  <svg class="abs" style="left:1000px;top:512px" width="58" height="44" viewBox="0 0 58 44"><g fill="#2f8fd0"><rect x="2" y="30" width="8" height="12"/><rect x="14" y="24" width="8" height="18"/><rect x="26" y="18" width="8" height="24"/><rect x="38" y="12" width="8" height="30"/></g><path d="M2 22L22 10L32 16L52 2" stroke="#2f8fd0" stroke-width="3" fill="none"/><path d="M44 2h8v8" stroke="#2f8fd0" stroke-width="3" fill="none"/></svg>
  <svg class="abs" style="left:890px;top:540px" width="120" height="30" viewBox="0 0 120 30"><path d="M0 28L118 2" stroke="#7fb6df" stroke-width="1.4"/></svg>
  <div class="feature-label" style="left:1020px;top:578px">ROI</div>
  <div class="feature-copy" style="left:780px;top:608px;width:320px;text-align:right">Identify the total revenue generated<br>vs. your campaign spend</div>

  <svg class="abs" style="left:768px;top:668px" width="56" height="50" viewBox="0 0 56 50"><g fill="#2f8fd0"><circle cx="18" cy="26" r="12"/><circle cx="40" cy="14" r="8"/></g><g fill="#f1f1f1"><circle cx="18" cy="26" r="5"/><circle cx="40" cy="14" r="3"/></g><g stroke="#2f8fd0" stroke-width="4"><line x1="18" y1="8" x2="18" y2="44"/><line x1="0" y1="26" x2="36" y2="26"/><line x1="40" y1="2" x2="40" y2="26"/><line x1="28" y1="14" x2="52" y2="14"/></g><g fill="#2f8fd0"><circle cx="18" cy="26" r="10"/></g><circle cx="18" cy="26" r="4" fill="#f1f1f1"/></svg>
  <svg class="abs" style="left:566px;top:640px" width="200" height="50" viewBox="0 0 200 50"><path d="M0 2L198 48" stroke="#7fb6df" stroke-width="1.4"/></svg>
  <div class="feature-label" style="left:758px;top:718px">Digital Leads</div>
  <div class="feature-copy" style="left:758px;top:748px;width:240px">View the leads SRM has generated for your business and identify the campaign source.</div>
</section>

<section class="cta">
  <div class="cta-text">SCHEDULE A DEMO TO SEE OUR FULL DASHBOARD IN ACTION</div>
  <div class="cta-btn">CLICK HERE</div>
</section>

<h2 class="section-title clients-title" style="font-size:25px">A Few Companies Who Love Us</h2>
<svg class="client-arrow" style="left:30px" width="26" height="70" viewBox="0 0 26 70"><path d="M22 2L4 35l18 33" stroke="#bbb" stroke-width="2" fill="none"/></svg>
<div class="client" style="left:136px">Arcline</div>
<div class="client" style="left:324px">Norvik</div>
<div class="client" style="left:512px">Helio</div>
<div class="client" style="left:700px">Quantra</div>
<div class="client" style="left:888px">Solenne</div>
<svg class="client-arrow" style="left:1138px" width="26" height="70" viewBox="0 0 26 70"><path d="M4 2l18 33L4 68" stroke="#bbb" stroke-width="2" fill="none"/></svg>

<section class="testimonials" role="img" aria-label="Photo of young plants growing in soil under a blue tint">
  <h2 class="section-title" style="top:46px;color:#fff;font-size:25px">The Word is Spreading</h2>
  <div class="bubble" style="left:136px">Lorem @ Ipsum is simply dummy text of the printing and typesetting industry. Lorem Ipsum has been the industry's standard.</div>
  <div class="bubble" style="left:459px">Lorem @ Ipsum is simply dummy text of the printing and typesetting industry. Lorem Ipsum has been the industry's standard. Read more...</div>
  <div class="bubble" style="left:782px">Lorem @ Ipsum is simply dummy text of the printing and typesetting industry. Lorem Ipsum has been the industry's standard.</div>
  <div class="author" style="left:150px"><div class="avatar"></div>Dana Whitfield (16 hours ago)</div>
  <div class="author" style="left:473px"><div class="avatar"></div>Dana Whitfield
    <svg width="74" height="14" viewBox="0 0 74 14"><g fill="#e67e22"><rect x="0" y="0" width="14" height="14"/><rect x="15" y="0" width="14" height="14"/><rect x="30" y="0" width="14" height="14"/><rect x="45" y="0" width="14" height="14"/><rect x="60" y="0" width="14" height="14"/></g><g fill="#fff"><polygon points="7,2 8.5,6 12,6 9,8.5 10,12 7,10 4,12 5,8.5 2,6 5.5,6"/><polygon points="22,2 23.5,6 27,6 24,8.5 25,12 22,10 19,12 20,8.5 17,6 20.5,6"/><polygon points="37,2 38.5,6 42,6 39,8.5 40,12 37,10 34,12 35,8.5 32,6 35.5,6"/><polygon points="52,2 53.5,6 57,6 54,8.5 55,12 52,10 49,12 50,8.5 47,6 50.5,6"/><polygon points="67,2 68.5,6 72,6 69,8.5 70,12 67,10 64,12 65,8.5 62,6 65.5,6"/></g></svg></div>
  <div class="author" style="left:796px"><div class="avatar"></div>Dana Whitfield (16 hours ago)</div>
</section>

<footer class="footer">Copyright © 2016 · Summitreach
  <svg class="abs" style="right:30px;top:6px" width="40" height="46" viewBox="0 0 40 46"><circle cx="20" cy="18" r="14" fill="#1b8fd6"/><path d="M13 21l7-7 7 7" stroke="#fff" stroke-width="3" fill="none"/><text x="20" y="44" font-size="8" fill="#aaa" text-anchor="middle" font-family="Open Sans, sans-serif">Back to top</text></svg>
</footer>

</body>
</html>
```